Redesign

Hello,

I want you to redesign this page: www.pravilo.com

I like the colors and would like to keep it 'airy', I don't want it to be the same boring website, although it needs to be easily navigational and user friendly.

NOTE: The websites main objective is to get people to signup to get our RSS services, the main task of the site is NOT a property search page, it is just a sub.

I am excited to see your designs.

Pages I am looking to have designed:
http://www.pravilo.com/
http://shortlinkory.com/q8vn27k
http://www.pravilo.com/advertise-your-real-estate.php
http://www.pravilo.com/submit-your-real-estate-listings.php
http://www.pravilo.com/2800/
http://www.pravilo.com/members/-/43

I HAVE POSTED A LARGER LOGO FOR YOU TO WORK WITH, I WANT THE LOGO TO BE INCORPORATED IN THE HEADER, NOT JUST STUCK THERE.

Owen
Updates

Hello,

I have made the project committed and I will chose one of your designs.

The current designs are nice but I really want the header to have the logo built into it, not have the logo just stuck in a box.

I also like the homepage designs with tiled sold homes, that is a great visual for the potential clients.

Thank you for your submissions so far.

Owen

Industry/Entity Type

Real Estate

```html
<!DOCTYPE html>
<html lang="en">
<head>
<meta charset="utf-8">
<title>Pravilo – Online Real Estate Marketing Simplified</title>
<link rel="stylesheet" href="https://fonts.googleapis.com/css2?family=Fjalla+One&family=Roboto:wght@400;500;700&display=swap">
<style>
:root{
  --blue:#1565b8;
  --blue-dark:#0d4f98;
  --navy:#0a3f7c;
  --sky-top:#2f7fd0;
  --sky-mid:#7db8ea;
  --sky-low:#d6ecfb;
  --grass:#6cae2c;
  --green:#7cbd2f;
  --green-dark:#5f9c1e;
  --red:#e2262e;
  --ink:#222;
  --muted:#666;
  --line:#d4d4d4;
  --panel:#efefef;
  --white:#fff;
}
*{box-sizing:border-box;margin:0;padding:0}
html,body{width:1200px;height:2553px;overflow:hidden;background:var(--white)}
body{font-family:Roboto,Arial,sans-serif;color:var(--ink);position:relative}
a{color:inherit;text-decoration:none}
.display{font-family:"Fjalla One",Impact,sans-serif;font-weight:400}

/* hero */
.hero{position:absolute;left:0;top:0;width:1200px;height:612px;overflow:hidden}
.hero-sky{position:absolute;inset:0;background:linear-gradient(180deg,var(--sky-top) 0%,#4f97dc 40%,var(--sky-mid) 70%,var(--sky-low) 88%)}
.hero-land{position:absolute;left:0;bottom:0;width:1200px;height:90px;background:linear-gradient(180deg,#b7dd6a 0%,var(--grass) 55%,#4f8f1c 100%)}
.topbar{position:absolute;left:0;top:0;width:1200px;height:75px;background:rgba(20,90,175,.55)}
.brand{position:absolute;left:172px;top:14px;display:flex;align-items:center;gap:8px;color:var(--white);font-size:38px;line-height:44px}
.brand-dot{width:14px;height:14px;border-radius:50%;background:#f5c21b}
.nav{position:absolute;left:383px;top:38px;display:flex;gap:26px;font-size:14px;color:var(--white)}
.nav a.active{border-bottom:2px solid var(--white);padding-bottom:6px}
.account{position:absolute;left:934px;top:38px;font-size:14px;color:var(--white);display:flex;align-items:center;gap:6px}
.account a{text-decoration:underline}
.feedback{position:absolute;left:0;top:160px;width:38px;height:122px;background:var(--blue);color:var(--white);border-radius:0 5px 5px 0;display:flex;align-items:center;justify-content:center}
.feedback span{transform:rotate(-90deg);font-size:15px;font-weight:700;white-space:nowrap}
.hero-title{position:absolute;left:0;top:148px;width:1200px;text-align:center;color:var(--white);font-size:70px;line-height:78px;text-shadow:0 2px 4px rgba(0,0,0,.2)}
.hero-sub{position:absolute;left:0;top:320px;width:1200px;text-align:center;color:var(--white);font-size:27px}
.btn{display:inline-flex;align-items:center;justify-content:center;gap:10px;color:var(--white);border-radius:5px;font-family:"Fjalla One",Impact,sans-serif;font-size:17px}
.btn-green{background:linear-gradient(180deg,#8fce3e,var(--green-dark))}
.btn-blue{background:linear-gradient(180deg,#1d74cc,var(--blue-dark))}
.hero-btn{position:absolute;left:498px;top:388px;width:204px;height:48px;font-size:19px}

/* intro */
.intro{position:absolute;left:158px;top:672px;width:470px}
.intro h2{font-size:23px;margin-bottom:18px}
.intro p{font-size:15px;line-height:21px;color:var(--muted);margin-bottom:20px}
.intro-actions{position:absolute;left:158px;top:912px;display:flex;gap:24px}
.intro-actions .btn{width:207px;height:46px}
.search{position:absolute;left:684px;top:672px;width:358px;height:172px;background:var(--blue);border-radius:6px;color:var(--white);text-align:center;padding-top:14px}
.search h3{font-size:28px;line-height:34px}
.search p{font-size:16px;line-height:20px;margin-top:4px}
.search-row{display:flex;justify-content:center;gap:6px;margin-top:16px}
.search-input{width:180px;height:30px;background:var(--white);border-radius:3px;color:#999;font-size:11px;text-align:left;padding:8px}
.search-row .btn{width:48px;height:30px;font-size:14px;border-radius:3px}
.search-note{position:absolute;left:684px;top:868px;width:358px;font-size:14px;line-height:19px;color:var(--muted)}
.search-note b{color:var(--ink)}

/* tree banner */
.pledge{position:absolute;left:158px;top:1034px;width:884px;height:148px;background:var(--blue);border-radius:6px;color:var(--white)}
.pledge-brand{position:absolute;left:30px;top:44px;width:170px;height:60px;background:var(--white);border-radius:4px;color:var(--blue);font-size:40px;display:flex;align-items:center;justify-content:center}
.pledge-copy{position:absolute;left:232px;top:26px;width:470px;display:flex;flex-direction:column;gap:12px}
.pledge-copy h3{font-size:20px;line-height:25px}
.pledge-copy p{width:420px;font-size:14px;line-height:19px}
.pledge .btn{position:absolute;left:722px;top:50px;width:133px;height:46px;font-size:16px}

/* properties */
.section-title{position:absolute;left:158px;top:1240px;width:884px;display:flex;align-items:center;gap:18px;font-size:23px}
.section-title::before,.section-title::after{content:"";flex:1;height:1px;background:var(--line)}
.card{position:absolute;width:434px;height:292px;border:1px solid var(--line);border-radius:4px;background:var(--white)}
.card-title{position:absolute;left:20px;top:14px;font-size:19px;white-space:nowrap}
.card-title small{font-family:Roboto,Arial,sans-serif;font-size:11px;color:var(--muted);text-transform:uppercase}
.card-photo{position:absolute;left:20px;top:48px;width:190px;height:158px;background:linear-gradient(180deg,#9cc4e6 0%,#c9b79a 55%,#6f8f4a 100%)}
.card-photo.alt{background:linear-gradient(180deg,#8fb8d8 0%,#b79e8a 50%,#5e8a3f 100%)}
.card-photo.palms{background:linear-gradient(180deg,#a9cbe6 0%,#6d9a55 55%,#4b7a36 100%)}
.tag{position:absolute;right:0;bottom:0;padding:4px 10px;font-size:11px;font-weight:700;color:var(--white)}
.tag-red{background:var(--red)}
.tag-blue{background:var(--blue)}
.price{position:absolute;left:218px;top:48px;width:196px;height:38px;background:var(--blue);color:var(--white);font-size:18px;line-height:38px;padding-left:8px}
.card-desc{position:absolute;left:220px;top:94px;width:190px;font-size:13px;line-height:18px;color:var(--muted)}
.more{position:absolute;left:220px;font-size:12px;color:var(--blue);display:flex;align-items:center;gap:6px}
.stats{position:absolute;left:0;bottom:0;width:432px;height:34px;background:var(--panel);border-top:1px solid var(--line);display:flex}
.stats span{flex:1;display:flex;align-items:center;justify-content:center;gap:6px;font-size:9px;color:var(--muted);border-right:1px solid var(--line)}
.stats span:last-child{border-right:0}
.stats svg{flex:none}

/* audience boxes */
.audience{position:absolute;top:1953px;width:282px;height:142px;background:var(--blue);border-radius:5px;color:var(--white);padding:16px 0 0 40px}
.audience h4{font-size:15px;margin-bottom:12px}
.audience li{list-style:none;font-size:12px;line-height:16px;margin-left:-4px}

/* cities */
.cities{position:absolute;left:0;top:2132px;width:1200px;height:376px;background:var(--panel)}
.cities h3{position:absolute;left:0;top:26px;width:1200px;text-align:center;font-size:25px}
.city-col{position:absolute;top:78px;list-style:none;font-size:11px;line-height:18px;color:var(--ink)}
.social{position:absolute;left:0;top:324px;width:1200px;display:flex;justify-content:center;gap:10px}
.social span{width:32px;height:32px;border-radius:50%}
.footer{position:absolute;left:0;top:2508px;width:1200px;height:45px;background:var(--navy);color:var(--white);text-align:center;font-size:11px;line-height:15px;padding-top:8px}
</style>
</head>
<body>

<header class="hero">
  <div class="hero-sky" role="img" aria-label="Bright blue sky with soft white clouds"></div>
  <div class="hero-land" role="img" aria-label="Green meadow with a lone tree and butterflies"></div>
  <div class="topbar"></div>
  <a class="brand display" href="#"><span>Pravilo</span><span class="brand-dot"></span></a>
  <nav class="nav">
    <a class="active" href="#">Home</a>
    <a href="#">Advertise your properties</a>
    <a href="#">Submit your listings</a>
    <a href="#">FAQ</a>
    <a href="#">Contact us</a>
  </nav>
  <div class="account">
    <svg width="14" height="14" viewBox="0 0 14 14"><circle cx="7" cy="4" r="3" fill="#fff"/><path d="M1 14c0-4 3-6 6-6s6 2 6 6z" fill="#fff"/></svg>
    <a href="#">Sign in</a> or <a href="#">Join</a>
  </div>
  <div class="feedback"><span>Feedback</span></div>
  <h1 class="hero-title display">Online Real Estate<br>Marketing Simplified</h1>
  <p class="hero-sub">PRAVILO provides the most exposure for real estate listings</p>
  <a class="btn btn-green hero-btn" href="#">Learn More</a>
</header>

<section class="intro">
  <h2 class="display">Online Real Estate Marketing Simplified</h2>
  <p>PRAVILO provides the most exposure for real estate listings. We have helped realtors, for sale by owners, for rent by owners, and many others promote their real estate.</p>
  <p>Listing your home on PRAVILO is easy and effective. Stop wasting your time managing multiple website listings and let PRAVILO do the work for you!</p>
</section>
<div class="intro-actions">
  <a class="btn btn-green" href="#">Submit Listings
    <svg width="16" height="16" viewBox="0 0 16 16"><rect x="2" y="2" width="12" height="12" rx="1" fill="none" stroke="#fff" stroke-width="2"/><path d="M5 8h6" stroke="#fff" stroke-width="2"/></svg></a>
  <a class="btn btn-blue" href="#">Submit RSS Feed
    <svg width="16" height="16" viewBox="0 0 16 16"><circle cx="3" cy="13" r="2" fill="#fff"/><path d="M1 7a8 8 0 0 1 8 8M1 2a13 13 0 0 1 13 13" fill="none" stroke="#fff" stroke-width="2"/></svg></a>
</div>

<aside class="search">
  <h3 class="display">Search Current Listings</h3>
  <p>Find your next home<br>or rental on PRAVILO today!</p>
  <div class="search-row">
    <div class="search-input">Enter a City and State or a Zip</div>
    <a class="btn btn-green" href="#">Buy</a>
    <a class="btn btn-green" href="#">Rent</a>
  </div>
</aside>
<p class="search-note"><b>Pravilo.com</b> markets your for sale or for rent properties to the most used real estate websites on the internet. Manage one listing and nightly we will update all of the other sites with your changes!</p>

<section class="pledge">
  <div class="pledge-brand display">Pravilo</div>
  <div class="pledge-copy">
    <h3 class="display">Pravilo.com is dedicated to creating a superior real state hub and is equally dedicated to preserv our planet.</h3>
    <p>For every single paid listing on Pravilo.com we will donate one tree to our conservation partner.</p>
  </div>
  <a class="btn btn-green" href="#">Advertise Today</a>
</section>

<h2 class="section-title display">Our Properties</h2>

<article class="card" style="left:158px;top:1294px">
  <h3 class="card-title display">Newer Home for Sale <small>| Surprise, AZ</small></h3>
  <div class="card-photo" role="img" aria-label="Photo of a single-storey stucco home with a two-car garage"><span class="tag tag-red">SOLD</span></div>
  <div class="price display">$439,000 - Home</div>
  <p class="card-desc">This is a 2 year old, Florida-style home in the Wellington Community of Maple Station. This home is truly a rare find.</p>
  <a class="more" href="#" style="top:196px">➤ More information</a>
  <div class="stats">
    <span><svg width="12" height="10"><rect width="12" height="10" fill="none" stroke="#777"/></svg>3000 sq ft</span>
    <span><svg width="14" height="10"><rect y="4" width="14" height="6" fill="#777"/><rect width="5" height="4" fill="#777"/></svg>3 Bedrooms</span>
    <span><svg width="14" height="10"><path d="M0 4h14v3a3 3 0 0 1-3 3H3a3 3 0 0 1-3-3z" fill="#777"/></svg>3 Bedrooms</span>
    <span><svg width="14" height="10"><path d="M0 4 7 0l7 4v6H0z" fill="#777"/></svg>2 Garages</span>
  </div>
</article>

<article class="card" style="left:608px;top:1294px">
  <h3 class="card-title display">Custom Built Home <small>| Syracuse, UT</small></h3>
  <div class="card-photo alt" role="img" aria-label="Photo of a two-storey brick home with a front lawn"></div>
  <div class="price display">$650,000 - Home</div>
  <p class="card-desc">Finding a home that reflects your lifestyle is important</p>
  <a class="more" href="#" style="top:140px">➤ More information</a>
  <div class="stats">
    <span><svg width="12" height="10"><rect width="12" height="10" fill="none" stroke="#777"/></svg>3000 sq ft</span>
    <span><svg width="14" height="10"><rect y="4" width="14" height="6" fill="#777"/><rect width="5" height="4" fill="#777"/></svg>3 Bedrooms</span>
    <span><svg width="14" height="10"><path d="M0 4h14v3a3 3 0 0 1-3 3H3a3 3 0 0 1-3-3z" fill="#777"/></svg>3 Bedrooms</span>
    <span><svg width="14" height="10"><path d="M0 4 7 0l7 4v6H0z" fill="#777"/></svg>2 Garages</span>
  </div>
</article>

<article class="card" style="left:158px;top:1608px">
  <h3 class="card-title display">Condo in Orlando <small>| Orlando, FL</small></h3>
  <div class="card-photo palms" role="img" aria-label="Photo of a condo complex lined with palm trees"><span class="tag tag-blue">BUY</span></div>
  <div class="price display">$5,000 - Condo</div>
  <p class="card-desc">Your condo comes equipped with amazing electronic features. For example, say you're expecting guests.</p>
  <a class="more" href="#" style="top:196px">➤ More information</a>
  <div class="stats">
    <span><svg width="12" height="10"><rect width="12" height="10" fill="none" stroke="#777"/></svg>3000 sq ft</span>
    <span><svg width="14" height="10"><rect y="4" width="14" height="6" fill="#777"/><rect width="5" height="4" fill="#777"/></svg>3 Bedrooms</span>
    <span><svg width="14" height="10"><path d="M0 4h14v3a3 3 0 0 1-3 3H3a3 3 0 0 1-3-3z" fill="#777"/></svg>3 Bedrooms</span>
    <span><svg width="14" height="10"><path d="M0 4 7 0l7 4v6H0z" fill="#777"/></svg>2 Garages</span>
  </div>
</article>

<article class="card" style="left:608px;top:1608px">
  <h3 class="card-title display">Condo Townhome <small>| Tampa, FL</small></h3>
  <div class="card-photo alt" role="img" aria-label="Photo of a lakeside townhome building"><span class="tag tag-red">RENT</span></div>
  <div class="price display">$990 - Condo</div>
  <p class="card-desc">A beautiful lakeside community, nestled in the heart of Carrollwood.</p>
  <a class="more" href="#" style="top:158px">➤ More information</a>
  <div class="stats">
    <span><svg width="12" height="10"><rect width="12" height="10" fill="none" stroke="#777"/></svg>3000 sq ft</span>
    <span><svg width="14" height="10"><rect y="4" width="14" height="6" fill="#777"/><rect width="5" height="4" fill="#777"/></svg>3 Bedrooms</span>
    <span><svg width="14" height="10"><path d="M0 4h14v3a3 3 0 0 1-3 3H3a3 3 0 0 1-3-3z" fill="#777"/></svg>3 Bedrooms</span>
    <span><svg width="14" height="10"><path d="M0 4 7 0l7 4v6H0z" fill="#777"/></svg>2 Garages</span>
  </div>
</article>

<section class="audience" style="left:158px">
  <h4 class="display">By Realtor</h4>
  <ul><li>Submit One Listing or Thousands</li><li>Promote Open Houses</li><li>Stand Out from the Competition</li><li>Self Promotion</li></ul>
</section>
<section class="audience" style="left:459px">
  <h4 class="display">By Owner</h4>
  <ul><li>Low Cost for Maximum Exposure</li><li>Easy to List &amp; Manage Your Property</li><li>Share with Social Networks &amp; Friends</li><li>Printable Flyer</li></ul>
</section>
<section class="audience" style="left:760px">
  <h4 class="display">Property Management</h4>
  <ul><li>RSS Feed Submission</li><li>One Stop Promo Shop</li><li>Expand Your Network</li><li>Simplified Marketing of Properties</li></ul>
</section>

<section class="cities">
  <h3 class="display">Popular Cities</h3>
  <ul class="city-col" style="left:158px"><li>Coconut Creek, FL</li><li>New Port Richey, FL</li><li>Port Richey, FL</li><li>Washington Terrace, UT</li><li>Allen, Texas</li><li>Garland, Texas</li><li>Ruskin, FL</li><li>Apollo Beach, FL</li><li>ORLANDO, FL</li><li>MESA, AZ</li><li>ORANGE PARK, FL</li><li>SAINT PETERSBURG, FL</li><li>HALLSVILLE, MO</li><li>NORTHAMPTON, PA</li></ul>
  <ul class="city-col" style="left:309px"><li>JACKSONVILLE, FL</li><li>Hooper, UT</li><li>Orange Park, Florida</li><li>Valrico, FL</li><li>Plant City, FL</li><li>Delray Beach, FL</li><li>Wesley Chapel, FL</li><li>Clearwater, Florida</li><li>Altamonte Springs, FL</li><li>Zephyrhills, FL</li><li>FARMINGTON, UT</li><li>Irving, Texas</li><li>Addison, Texas</li><li>Mansfield, Texas</li></ul>
  <ul class="city-col" style="left:460px"><li>ASTORIA, NY</li><li>Grapevine, Texas</li><li>BARTLETT, IL</li><li>Mesquite, Texas</li><li>PEORIA, AZ</li><li>PHILADELPHIA, PA</li><li>MEDFORD, OR</li><li>SHREVEPORT, LA</li><li>LAYTON, UT</li><li>SURPRISE, AZ</li><li>SYRACUSE, UT</li><li>Atlantic Beach, Florida</li><li>Temple Terrace, FL</li><li>Seminole, FL</li></ul>
  <ul class="city-col" style="left:610px"><li>Plantation, Florida</li><li>Plantation, Fl</li><li>Pinellas Park, FL</li><li>Kissimmee, FL</li><li>ROY, UT</li><li>CLINTON, UT</li><li>West Haven, UT</li><li>BOUNTIFUL, UT</li><li>KEY LARGO, FL</li><li>OGDEN, UT</li><li>JONESBOROUGH, TN</li><li>Richardson, Texas</li><li>Lewisville, Texas</li></ul>
  <ul class="city-col" style="left:759px"><li>ELIZABETHTON, TN</li><li>ISLAMORADA, FL</li><li>Sarasota, FL</li><li>Bradenton, FL</li><li>Palm Harbor, FL</li><li>KAYSVILLE, UT</li><li>Plano, Texas</li><li>Riverview, FL</li><li>Orlando, Florida</li><li>Lakeland, FL</li><li>McKinney, Texas</li><li>Frisco, Texas</li><li>ROCKFORD, IL</li></ul>
  <ul class="city-col" style="left:908px"><li>GLENDALE, AZ</li><li>St Petersburg, FL</li><li>PHOENIX, AZ</li><li>JOHNSON CITY, TN</li><li>Brandon, FL</li><li>Clearwater, FL</li><li>Orlando, FL</li><li>St. Petersburg, FL</li><li>Tampa, Florida</li><li>Dallas, Texas</li><li>Largo, FL</li><li>ATLANTIC CITY, NJ</li><li>Seminole, FL</li></ul>
  <div class="social">
    <span style="background:#3b5fa8"></span>
    <span style="background:#2fa7e0"></span>
    <span style="background:#f07a22"></span>
  </div>
</section>

<footer class="footer">
  <div>Home | Listbase RSS Feed Replacement | Submit Your Listings | Contact Pravilo</div>
  <div>© 2012 Pravilo LLC. All rights reserved.</div>
</footer>

</body>
</html>
```